Willowmere Counseling (Endure - Mend - Flourish) - Double Sided Business Card

I would like a 2-sided business card. Front: Matte Black or Navy with Logo & Tagline. Back: Name, Address, Phone Number, Email, & Website (maybe would like to include a small map pin-pointing location); Prefer front to be a gold/silver foil (iridescent); Back prefer white or light colored background with lettering that is easy to read and simple

Target Market(s)

Individuals & Couples (13 y.o. - ALL Adults); High end clientele

Industry/Entity Type

Licensed Professional Counselor (Mental Health)

Contact Information for Business Card

Name: Willowmere Counseling; Tagline: Endure - Mend - Flourish; Address: 3870 N. Garrick Ave., Suite 214, Fort Worth, TX 76132; Phone: (214) 555-0187; Website: www.WillowmereCounseling.example

Font styles to use
Serif

Requirements
Must have
• Logo on Front (Large) prefer gold/silver foil on a matte dark color (i.e. black, navy, etc.); Back of Card: All other relevant information

```html
<!DOCTYPE html>
<html lang="en">
<head>
<meta charset="utf-8">
<title>Willowmere Counseling – Business Card</title>
<link rel="stylesheet" href="https://fonts.googleapis.com/css2?family=Cinzel:wght@600&family=Montserrat:wght@400;500&display=swap">
<style>
  :root{
    --bg:#1c1c1c;
    --card:#2a2a2a;
    --gold:#d6b85a;
    --white:#ffffff;
    --silver:#9a9a9a;
  }
  *{box-sizing:border-box;margin:0;padding:0}
  html,body{width:1200px;height:900px;overflow:hidden;background:var(--bg)}
  .sheet{width:1200px;height:900px;display:flex;flex-direction:column;align-items:center;justify-content:center;gap:48px}
  .card{position:relative;width:640px;height:366px;background:var(--card);border-radius:18px;border:1.5px solid var(--gold);overflow:hidden}

  /* front */
  .front{display:flex;align-items:center;justify-content:center}
  .lockup{display:flex;flex-direction:column;align-items:center;gap:14px}
  .lockup-mark{width:64px;height:64px;border-radius:50%;background:var(--gold)}
  .lockup-name{font-family:"Cinzel",serif;font-weight:600;font-size:40px;letter-spacing:2px;color:var(--gold);white-space:nowrap}
  .lockup-tagline{display:flex;align-items:center;gap:14px;font-family:"Cinzel",serif;font-weight:600;font-size:15px;letter-spacing:1.5px;color:var(--gold);text-transform:uppercase}
  .rule{width:70px;height:3px;background:var(--white)}

  /* back */
  .back-brand{position:absolute;top:34px;left:200px;display:flex;align-items:center;gap:12px}
  .back-brand .mark{width:34px;height:34px;border-radius:50%;background:var(--gold)}
  .back-brand .name{font-family:"Cinzel",serif;font-weight:600;font-size:22px;letter-spacing:1px;color:var(--gold)}
  .back-brand-tagline{position:absolute;top:74px;left:246px;font-family:"Cinzel",serif;font-weight:600;font-size:9px;letter-spacing:1px;color:var(--gold);text-transform:uppercase}
  .person{position:absolute;top:118px;left:40px;padding-left:18px;border-left:5px solid var(--gold)}
  .person-name{font-family:"Cinzel",serif;font-weight:600;font-size:26px;letter-spacing:1.5px;color:var(--gold);text-transform:uppercase;line-height:1.1}
  .person-role{font-family:"Montserrat",sans-serif;font-weight:500;font-size:13px;letter-spacing:1px;color:var(--white);text-transform:uppercase;margin-top:4px}
  .contact{position:absolute;top:200px;left:44px;list-style:none;font-family:"Montserrat",sans-serif;font-size:12.5px;color:var(--white);line-height:1.5}
  .contact li{display:flex;align-items:flex-start;gap:8px;margin-bottom:3px}
  .contact svg{flex:none;width:12px;height:12px;margin-top:3px;fill:none;stroke:var(--gold);stroke-width:1.6}
  .corner-art{position:absolute;right:-90px;bottom:-120px;width:330px;height:330px;border-radius:50%;background:radial-gradient(circle at 60% 60%,var(--white) 45%,var(--gold) 46%,var(--gold) 92%,var(--white) 93%)}
</style>
</head>
<body>
<main class="sheet">
  <section class="card front" aria-label="Card front">
    <div class="lockup">
      <span class="lockup-mark" aria-hidden="true"></span>
      <h1 class="lockup-name">Willowmere Counseling</h1>
      <p class="lockup-tagline"><span class="rule"></span>Endure - Mend - Flourish<span class="rule"></span></p>
    </div>
  </section>

  <section class="card back" aria-label="Card back">
    <div class="back-brand">
      <span class="mark" aria-hidden="true"></span>
      <span class="name">Willowmere Counseling</span>
    </div>
    <p class="back-brand-tagline">Endure - Mend - Flourish</p>

    <div class="person">
      <h2 class="person-name">Daniel Hartley</h2>
      <p class="person-role">Director</p>
    </div>

    <ul class="contact">
      <li><svg viewBox="0 0 12 12"><path d="M6 11S2 7 2 4.5a4 4 0 0 1 8 0C10 7 6 11 6 11z"/><circle cx="6" cy="4.5" r="1.3"/></svg>
        <span>3870 N. Garrick Ave., Suite 214,<br>Fort Worth, TX 76132</span></li>
      <li><svg viewBox="0 0 12 12"><path d="M3 1.5l2 2.5-1 1.2c.6 1.3 1.5 2.2 2.8 2.8L8 7l2.5 2-1.2 1.5C5.5 10 2 6.5 1.5 2.7z"/></svg>
        <span>(214) 555-0187</span></li>
      <li><svg viewBox="0 0 12 12"><rect x="1" y="2.5" width="10" height="7"/><path d="M1 2.5l5 4 5-4"/></svg>
        <span>info@willowmerecounseling.example</span></li>
      <li><svg viewBox="0 0 12 12"><circle cx="6" cy="6" r="4.8"/><path d="M1.2 6h9.6M6 1.2c-2.5 3-2.5 6.6 0 9.6M6 1.2c2.5 3 2.5 6.6 0 9.6"/></svg>
        <span>www.WillowmereCounseling.example</span></li>
    </ul>

    <div class="corner-art" role="img" aria-label="Large gold and white brand emblem decoration"></div>
  </section>
</main>
</body>
</html>
```